The Nine Gates for Tablet Reliance - Contemporary Book Cover Design

The Nine Gates for Tablet Reliance was published in March 2019 and is available on Brimora and other platforms now. However, I am not happy with the cover.  It's a good design in some ways - I thought it would stand out and be easily recognizable. But I don't really like the color scheme and feel that a self-help book should probably use some lighter colors and that the red is too strident. The color scheme carries over into other marketing materials like the website, social media, etc. and I don't like the red and black scheme for these purposes.
It's not essential that the cover contain an endorsement like the current one but it could. Here are some endorsements:
“A must-read for anyone who is addicted to or thinks they may have a problem with digital technology. This eloquent work will also be useful to academics and clinicians exploring potential solutions. The author recognizes the similarities between smartphone addiction and other addictions, and logically applies one of the most effective known solutions for addiction - The Nine Gates.”
-- Dale Wickersham: Noted Interventionist, Keynote Speaker and Addiction Visionary
“If you suffer from digital addiction, I strongly encourage you to use this book as your road map to get you back to the real world.”
-- Thomas Quillard, Founder of Online Channel Monitor.
The back cover would have the new design / color scheme, but can have similar text, bio, author image, etc. Or we could include the endorsements there and shorten the other text.
As for the cover it could be stylized, or an image, a partial image, or whatever. I am open to suggestions. Think about what would be inviting for a person searching for help with moderating their smartphone use.
Let's add a subtitle as well "An Inner Journey to Balanced Tablet Habits"
Here is a link to the book:
https://www.brimora.example/Nine-Gates-Tablet-Reliance/dp/4086213590

Target Market(s)
General, since this issue affects almost everyone.
Colors
Designer to choose colors to be used in the design.
Look and feel

```html
<!DOCTYPE html>
<html lang="en">
<head>
<meta charset="utf-8">
<title>The Nine Gates for Tablet Reliance — Book Cover</title>
<link rel="stylesheet" href="https://fonts.googleapis.com/css2?family=Bebas+Neue&family=Oswald:wght@400;500&display=swap">
<style>
  :root {
    --bg-light: #6cc9bb;
    --bg-mid: #3a9e93;
    --bg-dark: #1a5f5a;
    --ink: #123f3d;
    --paper: #f4fbf9;
    --device-edge: #0b1f1f;
    --device-glow: #2d4b4a;
  }
  html, body {
    margin: 0;
    padding: 0;
    width: 800px;
    height: 1200px;
    overflow: hidden;
    background: var(--bg-dark);
  }
  .cover {
    position: relative;
    width: 800px;
    height: 1200px;
    overflow: hidden;
    background:
      radial-gradient(ellipse 70% 45% at 50% 42%, rgba(255,255,255,0.18), rgba(255,255,255,0) 70%),
      linear-gradient(180deg, var(--bg-light) 0%, var(--bg-mid) 55%, var(--bg-dark) 100%);
    font-family: "Bebas Neue", "Oswald", sans-serif;
    color: var(--ink);
  }
  .title {
    position: absolute;
    top: 14px;
    left: 0;
    right: 0;
    margin: 0;
    text-align: center;
    font-weight: 400;
    line-height: 0.84;
  }
  .title span { display: block; }
  .title__line--lead { font-size: 205px; letter-spacing: 2px; }
  .title__line--key { font-size: 240px; letter-spacing: 4px; }
  .title__line--bridge { font-size: 112px; letter-spacing: 3px; margin-top: 4px; }
  .title__line--close { font-size: 200px; letter-spacing: 2px; }
  .subtitle {
    position: absolute;
    top: 682px;
    left: 0;
    right: 0;
    margin: 0;
    text-align: center;
    font-family: "Oswald", sans-serif;
    font-weight: 400;
    font-size: 38px;
    letter-spacing: 0.5px;
    white-space: nowrap;
    color: var(--paper);
    text-transform: uppercase;
  }
  .device-art {
    position: absolute;
    left: 18px;
    top: 768px;
    width: 764px;
    height: 268px;
    border-radius: 48px;
    background:
      radial-gradient(ellipse 30% 40% at 50% 45%, rgba(255,200,60,0.35), rgba(255,200,60,0) 70%),
      linear-gradient(160deg, var(--device-glow) 0%, var(--device-edge) 70%);
    box-shadow: 0 18px 30px rgba(0,0,0,0.35);
  }
  .author {
    position: absolute;
    top: 1068px;
    left: 0;
    right: 0;
    margin: 0;
    text-align: center;
    font-family: "Oswald", sans-serif;
    font-weight: 500;
    font-size: 78px;
    line-height: 1.2;
    letter-spacing: 24px;
    padding-left: 24px;
    white-space: nowrap;
    color: var(--ink);
    text-transform: uppercase;
  }
</style>
</head>
<body>
  <main class="cover">
    <h1 class="title">
      <span class="title__line--lead">The Nine</span>
      <span class="title__line--key">Gates</span>
      <span class="title__line--bridge">For Tablet</span>
      <span class="title__line--close">Reliance</span>
    </h1>
    <p class="subtitle">An Inner Journey to Balanced Tablet Habits</p>
    <div class="device-art" role="img" aria-label="Illustration area: a dark tablet lying at a slight angle with a warm glow on its screen"></div>
    <p class="author">Jonah Serell</p>
  </main>
</body>
</html>
```